KTRWG Promotion Flyer to raise money and communicate our goals

We need a flyer that promotes our organization. We are a 501(c)3 trying to raise money for Arts, Education and Entrepreneurship in our small town.

We promote a social events that improve qualtiy of life and educate people on how to start and expand businesses. Our goal is to make downtown an active and thriving place with many things for people to do and enjoy as well as create a favorable place for business.

Target Market(s)

Wealthy donors and Organizations with cash

Industry/Entity Type

Education

Colors

Designer to choose colors to be used in the design.

Requirements
Must have
• Eye catching graphics and look very professional
• Should appeal to men and women
Nice to have
• Make use of any known psychological colors and fonts etc... that appeal to philanthropic people
Should not have
• Should not be complicated or confusing

```html
<!DOCTYPE html>
<html lang="en">
<head>
<meta charset="utf-8">
<title>KTRWG Flyer</title>
<link href="https://fonts.googleapis.com/css2?family=Lato:wght@300;400;700;900&display=swap" rel="stylesheet">
<style>
:root{
  --stage:#bfc0c2;
  --pink:#e5176f;
  --blue:#1ba1dc;
  --green:#7ab93d;
  --ink:#3a3a3a;
  --panel:#f7f7f5;
  --white:#ffffff;
}
*{margin:0;padding:0;box-sizing:border-box}
html,body{width:967px;height:1200px;overflow:hidden}
body{background:var(--stage);font-family:'Lato',sans-serif;color:var(--ink);position:relative}
.flyer{position:absolute;left:46px;top:39px;width:865px;height:1119px;overflow:hidden;box-shadow:4px 5px 10px rgba(0,0,0,.35);background:var(--white)}
.flyer-art{position:absolute;inset:0;width:100%;height:100%}
.brand{position:absolute;left:70px;top:80px;display:flex;align-items:center;gap:12px;font-weight:700;font-size:38px;color:#4a4a4a;letter-spacing:1px}
.brand-square{width:34px;height:34px;background:var(--blue)}
.tagline-banner{position:absolute;left:0;top:223px;width:248px;height:125px;background:var(--pink);clip-path:polygon(0 0,100% 0,96% 100%,0 100%);color:var(--white);font-weight:700;font-size:20px;line-height:25px;padding:13px 0 0 27px;text-transform:uppercase}
.intro,.appeal{position:absolute;left:338px;font-size:17.3px;line-height:23.4px;color:var(--ink)}
.intro{top:94px;width:475px}
.appeal{top:625px;width:490px}
.pledge{position:absolute;left:338px;width:505px}
.pledge-label{position:absolute;left:0;top:3px;width:127px;height:27px;background:var(--blue);color:var(--white);font-weight:700;font-size:17.5px;line-height:27px;padding-left:10px}
.pledge-text{position:absolute;left:142px;top:0;width:340px;font-size:17.3px;line-height:23.4px}
.donate-button{position:absolute;left:407px;top:926px;width:348px;height:37px;background:var(--pink);border-radius:4px;color:var(--white);font-weight:700;font-size:21px;line-height:37px;text-align:center}
.join-banner{position:absolute;left:0;top:974px;width:270px;height:107px;background:var(--green);clip-path:polygon(0 0,72% 0,100% 100%,0 100%);color:var(--white);padding:10px 0 0 27px}
.join-banner .join-line{font-weight:300;font-size:34px;line-height:38px}
.join-banner .join-strong{font-weight:900;font-size:38px;line-height:44px}
</style>
</head>
<body>
<div class="flyer">
  <svg class="flyer-art" viewBox="0 0 850 1100" preserveAspectRatio="none">
    <defs>
      <linearGradient id="sceneTone" x1="0" y1="0" x2="0" y2="1">
        <stop offset="0" stop-color="#e4eaee"/>
        <stop offset="0.35" stop-color="#cfd6d8"/>
        <stop offset="0.45" stop-color="#b9ad9c"/>
        <stop offset="0.58" stop-color="#6f8f4a"/>
        <stop offset="0.88" stop-color="#5f8a3c"/>
        <stop offset="0.9" stop-color="#7a7a78"/>
        <stop offset="1" stop-color="#6d9447"/>
      </linearGradient>
      <linearGradient id="panelTone" x1="0" y1="0" x2="0" y2="1">
        <stop offset="0" stop-color="#f4f5f3"/>
        <stop offset="0.5" stop-color="#efefec"/>
        <stop offset="1" stop-color="#f8f8f7"/>
      </linearGradient>
    </defs>
    <rect width="850" height="1100" fill="url(#sceneTone)" role="img" aria-label="Photo of the town's community hall with a gazebo, trees and lawn"/>
    <path d="M330 0 L850 0 L850 905 C700 918 460 955 345 950 C250 942 200 860 195 720 C190 560 200 420 240 300 C270 200 290 80 330 0 Z" fill="url(#panelTone)" role="img" aria-label="Faint misty pine forest behind the text"/>
    <path d="M295 68 C315 35 335 10 362 0 L600 0 C480 8 370 28 295 68 Z" fill="var(--green)"/>
  </svg>

  <div class="brand"><span class="brand-square"></span>KTRWG</div>

  <div class="tagline-banner">Arts, Education and Entrepreneurship in Larkfield</div>

  <p class="intro">The Larkfield Small Business Association (KTRWG) is a local leader in the areas of Arts, Education and Entrepreneurship and is working diligently to promote Larkfield and revitalize our downtown. When you become an KTRWG Member, you will be a part of the citywide work that the KTRWG does every day to improve the lives of citizens of Larkfield.</p>

  <div class="pledge" style="top:295px">
    <span class="pledge-label">We promote</span>
    <p class="pledge-text">Larkfield Hotels, Shopping and Events that make Larkfield a pleasant, exciting and prosperous place to live.</p>
  </div>
  <div class="pledge" style="top:387px">
    <span class="pledge-label">We provide</span>
    <p class="pledge-text">Training and resources to anyone interested Arts, Education and Entrepreneurship.</p>
  </div>
  <div class="pledge" style="top:460px">
    <span class="pledge-label">We help</span>
    <p class="pledge-text">Entrepreneur’s start and grow their businesses in a tax<br>efficient and appropriate way.</p>
  </div>
  <div class="pledge" style="top:529px">
    <span class="pledge-label">We work</span>
    <p class="pledge-text">With all levels of local government to promote our community and create a fertile environment for growth.</p>
  </div>

  <p class="appeal">Every day, we look for ways to help our local businesses grow and expand, but we need you by our side. As an KTRWG Member, you can help provide training, educa­tion and support, and you can give our many businesses a chance to grow and our citizens the opportunity to expe­rience big town amenities and events in a small town. Members' regular monthly gifts provide a consistent, reliable income stream that allows us to spend less time fundraising—and more time helping our businesses and community. Becoming an KTRWG Member is an easy, efficient and tax-deductible way to make a difference for our community all year long.</p>

  <div class="donate-button">PLEASE DONATE TODAY.</div>

  <div class="join-banner">
    <div class="join-line">JOIN US</div>
    <div class="join-strong">TODAY!</div>
  </div>
</div>
</body>
</html>
```